Single Page website for Product Company

I need a website designed for my small startup company "Lantern Yard Furnishings". We design and manufacture custom innovative indoor/outdoor entertainment furnishings e.g. outdoor TV enclosures, outdoor bars and outdoor kitchens. I'm looking for a single page site based on the the tinyShelf-SoloView-storefront bootstrap page, attached.

I've also attached pictures of my products, these need to be photoshopped and placed in an outdoor patio area if possible.

Target Market(s)

Home owners

Industry/Entity Type

It Company

Coding

Coded - Design and coding required

Number of Pages Required

1 page

Requirements
Must have
• Must be single page site built with attached bootstrap template and adjust to screen size e.g. ipad, mobile phone and computer
Nice to have
• Integration with vendaro

```html
<!DOCTYPE html>
<html lang="en">
<head>
<meta charset="utf-8">
<title>Lantern Yard Furnishings</title>
<link href="https://fonts.googleapis.com/css2?family=Open+Sans:wght@400;600;700&display=swap" rel="stylesheet">
<style>
:root{
  --orange:#f7941d;
  --orange-dark:#e07f0c;
  --blue:#45a6ef;
  --ink:#2b2b2b;
  --text:#555;
  --muted:#8a8a8a;
  --line:#e3e3e3;
  --grey-band:#f2f2f2;
  --footer-bg:#f5f5f5;
  --dark:#1d1d1d;
  --white:#fff;
}
*{box-sizing:border-box;margin:0;padding:0}
html,body{width:1200px;height:4138px;overflow:hidden}
body{font-family:"Open Sans",Arial,sans-serif;color:var(--text);background:var(--white);position:relative;font-size:14px}
section,header,footer{position:absolute;left:0;width:1200px}
.abs{position:absolute}
.btn{position:absolute;display:flex;align-items:center;justify-content:center;background:var(--orange);color:var(--white);font-weight:700;font-size:13px;border-radius:6px;border:2px solid var(--orange-dark);text-transform:uppercase;letter-spacing:.5px}
.field{position:absolute;background:var(--white);border:1px solid #d8d8d8;border-radius:5px;font-size:13px;color:#888;padding:0 14px;display:flex;align-items:center}
.section-title{position:absolute;left:0;width:1200px;text-align:center;font-size:22px;font-weight:600;color:var(--ink);letter-spacing:.5px}

/* hero */
.hero{top:0;height:571px}
.hero-photo{position:absolute;inset:0;background:linear-gradient(180deg,#3a3734 0%,#4d4843 45%,#6a5a48 70%,#5a4f45 100%)}
.hero-shade{position:absolute;inset:0;background:rgba(0,0,0,.35)}
.topbar{position:absolute;top:0;left:0;width:1200px;height:88px;background:rgba(20,20,20,.6)}
.brand{position:absolute;left:94px;top:26px;display:flex;align-items:center;gap:10px;color:var(--white);font-weight:600;font-size:18px}
.brand-mark{width:16px;height:16px;background:var(--orange)}
.nav a{position:absolute;top:34px;color:var(--white);font-size:13px;font-weight:700;text-decoration:none;letter-spacing:.3px}
.nav a.active{color:var(--orange)}
.lang{position:absolute;left:1071px;top:22px;width:40px;height:39px;background:var(--orange);border-radius:5px;color:var(--white);font-size:13px;font-weight:700;display:flex;align-items:center;justify-content:center}
.hero-title{position:absolute;top:222px;left:0;width:1200px;text-align:center;color:var(--white);font-size:30px;font-weight:600}
.hero-lead{position:absolute;top:292px;left:320px;width:560px;text-align:center;color:#eee;font-size:13.5px;line-height:21px}
.hero-buy{left:544px;top:386px;width:113px;height:47px;background:transparent;color:var(--orange);border:2px solid var(--orange);font-weight:600}
.dots{position:absolute;left:0;width:1200px;display:flex;justify-content:center;gap:8px}
.dots i{width:10px;height:10px;border-radius:50%;border:2px solid var(--white);display:block}
.dots i.on{background:var(--white)}
.arrow{position:absolute;top:268px}

/* products */
.products{top:571px;height:511px}
.card{position:absolute;top:157px;width:325px}
.card-photo{height:232px;border-radius:8px}
.card-name{position:absolute;top:268px;left:0;color:var(--orange);font-size:16px;font-weight:600}
.card-price{position:absolute;top:268px;right:0;color:var(--ink);font-size:16px}

/* shipping band */
.shipping{top:1082px;height:176px;background:var(--grey-band)}
.shipping-text{position:absolute;left:86px;top:70px;font-size:27px;color:var(--ink)}
.count{position:absolute;top:72px;width:40px;height:36px;background:var(--white);border:1px solid #ddd;border-radius:3px;display:flex;align-items:center;justify-content:center;font-size:15px;color:var(--ink)}
.count.first{color:var(--orange)}

/* about */
.about{top:1258px;height:309px}
.about h2{position:absolute;left:86px;top:80px;font-size:20px;font-weight:700;color:var(--ink);letter-spacing:.5px}
.about-sub{position:absolute;left:86px;top:112px;font-size:15px;color:var(--muted)}
.about-body{position:absolute;left:500px;top:12px;width:615px;font-size:12.5px;line-height:22px;color:var(--text)}

/* testimonial */
.quote{top:1567px;height:345px}
.quote-photo{position:absolute;inset:0;background:linear-gradient(180deg,#2a241f 0%,#3b3026 55%,#4a3a2c 100%)}
.quote-text{position:absolute;top:68px;left:0;width:1200px;text-align:center;color:var(--white);font-size:25px;line-height:42px}
.quote-name{position:absolute;top:168px;left:0;width:1200px;text-align:center;color:var(--orange);font-size:20px}

/* newsletter */
.newsletter{top:1912px;height:259px;background:var(--blue)}
.newsletter h2{position:absolute;top:52px;left:0;width:1200px;text-align:center;color:var(--white);font-size:23px;font-weight:700}
.newsletter p{position:absolute;top:98px;left:0;width:1200px;text-align:center;color:#e6f2fc;font-size:15px}

/* order form */
.order{top:2171px;height:1099px}
.order-table{position:absolute;left:86px;top:160px;width:1029px}
.row{position:relative;height:69px;border-bottom:2px solid #f6c48a;font-size:14px;color:#777}
.row.head{height:50px;color:var(--ink);font-size:16px;font-weight:600}
.row span{position:absolute;top:22px}
.row.head span{top:8px}
.qty{position:absolute;top:16px;left:614px;width:56px;height:32px;border:1px solid #d5d5d5;border-radius:4px;background:var(--white)}
.qty b{position:absolute;right:0;top:0;width:20px;height:30px;background:#999;border-radius:0 3px 3px 0}
.sub-title{position:absolute;font-size:17px;font-weight:600;color:var(--ink);text-align:center}
.select b{position:absolute;right:0;top:0;width:22px;height:100%;background:#aaa;border-radius:0 4px 4px 0}
.sum-row{position:absolute;left:640px;width:468px;font-size:12.5px;color:#777;display:flex;justify-content:space-between;border-top:1px solid var(--line);padding-top:12px}

/* features */
.features{top:3270px;height:234px;background:var(--blue)}
.feature{position:absolute;top:86px;width:260px;text-align:center;color:var(--white);font-size:16px;font-weight:600}
.feature svg{display:block;margin:0 auto 16px}

/* contact */
.contact{top:3504px;height:524px;background:var(--footer-bg)}
.contact h3{position:absolute;font-size:20px;font-weight:700;color:var(--ink)}
.info{position:absolute;left:138px;display:flex;gap:18px;font-size:12.5px;color:#666;line-height:18px}
.info .ico{width:40px;height:40px;border-radius:50%;border:2px solid #f6c48a;display:flex;align-items:center;justify-content:center;flex:none}

/* bottom bar */
.bottom{top:4028px;height:110px;background:var(--dark)}
.bottom p{position:absolute;left:86px;top:46px;color:#bbb;font-size:12.5px}
</style>
</head>
<body>

<header class="hero">
  <div class="hero-photo" role="img" aria-label="Two large outdoor TVs mounted above a stone entertainment enclosure with blue-lit speakers"></div>
  <div class="hero-shade"></div>
  <div class="topbar">
    <div class="brand"><span class="brand-mark"></span>Lantern Yard Furnishings</div>
    <nav class="nav">
      <a class="active" style="left:506px">PRODUCTS</a>
      <a style="left:624px">ABOUT</a>
      <a style="left:719px">ORDER</a>
      <a style="left:810px">CONTACT</a>
      <a style="left:923px">EXTERNAL LINK</a>
    </nav>
    <div class="lang">UK</div>
  </div>
  <svg class="arrow" style="left:40px" width="20" height="28" viewBox="0 0 20 28"><path d="M15 3 5 14l10 11" fill="none" stroke="#ddd" stroke-width="3"/></svg>
  <svg class="arrow" style="left:1140px" width="20" height="28" viewBox="0 0 20 28"><path d="M5 3l10 11-10 11" fill="none" stroke="#ddd" stroke-width="3"/></svg>
  <h1 class="hero-title">Lantern Yard Furnishings</h1>
  <p class="hero-lead">Lorem ipsum dolor sit amet, consectetur adipiscing elit. Nam sapien risus, blandit at fringilla ac, varius sed dolor. Donec augue lacus, vulputate sed consectetur facilisis, interdum pharetra ligula. Nulla suscipit erat nibh, ut porttitor nisl dapibus eu.</p>
  <div class="btn hero-buy">Buy $800</div>
  <div class="dots" style="top:519px"><i class="on"></i><i></i><i></i></div>
</header>

<section class="products">
  <h2 class="section-title" style="top:76px">PRODUCTS</h2>
  <div class="card" style="left:86px">
    <div class="card-photo" role="img" aria-label="Wooden TV stand cabinet with built-in speakers" style="background:linear-gradient(180deg,#d79a45,#c6873a)"></div>
    <div class="card-name">TV Stand</div><div class="card-price">$700</div>
  </div>
  <div class="card" style="left:439px">
    <div class="card-photo" role="img" aria-label="Stone TV enclosure with blue-lit speakers" style="background:linear-gradient(180deg,#6b625a,#c9b9a4)"></div>
    <div class="card-name">Finibus Bonorum</div><div class="card-price">$400</div>
  </div>
  <div class="card" style="left:789px">
    <div class="card-photo" role="img" aria-label="Stone entertainment wall with mounted TV" style="background:linear-gradient(180deg,#8d8780,#d6ccbf)"></div>
    <div class="card-name">Et Malorum</div><div class="card-price">$600</div>
  </div>
</section>

<section class="shipping">
  <p class="shipping-text">Free international shipping only 2 days :</p>
  <div class="count first" style="left:588px">23</div>
  <div class="count" style="left:635px">32</div>
  <div class="count" style="left:682px">48</div>
  <div class="btn" style="left:988px;top:68px;width:121px;height:42px;font-size:15px;text-transform:none">Order Now</div>
</section>

<section class="about">
  <h2>ABOUT LANTERN YARD</h2>
  <p class="about-sub">Pellentesque interdum eget</p>
  <p class="about-body">Pellentesque interdum eget odio eu rutrum. Nunc tempus massa a tellus aliquet sodales. Nunc urna tortor, rhoncus accumsan viverra lorem ipsum has been the industry's standard dummy text ever since the 1500s, when an unknown printer took a galley of type and scrambled it, feugiat a mauris. In hac habitasse platea dictumst. In sagittis orci nec aliquet tristique.</p>
  <div class="btn" style="left:502px;top:193px;width:111px;height:39px;font-size:12px">Read More</div>
</section>

<section class="quote">
  <div class="quote-photo" role="img" aria-label="Dark close-up of stacked wooden logs"></div>
  <p class="quote-text">This is one of the most beautiful site I have ever seen in my life<br>Your site is great!</p>
  <p class="quote-name">- Dana Whitfield -</p>
  <div class="dots" style="top:255px"><i class="on"></i><i></i><i></i></div>
</section>

<section class="newsletter">
  <h2>STAY IN TOUCH</h2>
  <p>Sign Up for Email Updates on on News &amp; Offers</p>
  <div class="field" style="left:292px;top:160px;width:483px;height:44px;border:none">Enter Mail</div>
  <div class="btn" style="left:797px;top:160px;width:111px;height:44px;font-size:12px">Subscribe</div>
</section>

<section class="order">
  <h2 class="section-title" style="top:72px">ORDER FORM</h2>
  <div class="order-table">
    <div class="row head"><span style="left:0">Product</span><span style="left:299px">Unit Cost</span><span style="left:614px">Quantity</span><span style="left:950px">Total</span></div>
    <div class="row"><span style="left:0">TV Stand</span><span style="left:299px">$700</span><div class="qty"><span style="left:10px;top:6px;font-size:12px">0</span><b></b></div><span style="left:950px">$0</span></div>
    <div class="row"><span style="left:0">Finibus Bonorum</span><span style="left:299px">$400</span><div class="qty"><span style="left:10px;top:6px;font-size:12px">0</span><b></b></div><span style="left:950px">$0</span></div>
    <div class="row"><span style="left:0">Et Malorum</span><span style="left:299px">$600</span><div class="qty"><span style="left:10px;top:6px;font-size:12px">0</span><b></b></div><span style="left:950px">$0</span></div>
  </div>

  <h3 class="sub-title" style="left:86px;width:449px;top:487px">Payment Method</h3>
  <div class="field" style="left:91px;top:544px;width:287px;height:44px">Card Number</div>
  <div class="field" style="left:392px;top:544px;width:141px;height:44px">Code</div>
  <div class="field select" style="left:91px;top:605px;width:204px;height:44px">January<b></b></div>
  <div class="field select" style="left:334px;top:605px;width:199px;height:44px">2014<b></b></div>
  <h3 class="sub-title" style="left:86px;width:449px;top:708px">Information</h3>
  <div class="field" style="left:91px;top:765px;width:217px;height:44px">First Name</div>
  <div class="field" style="left:320px;top:765px;width:213px;height:44px">Last Name</div>
  <div class="field" style="left:91px;top:831px;width:442px;height:44px">Your Email</div>
  <h3 class="sub-title" style="left:86px;width:449px;top:922px">If you have Coupon code</h3>
  <div class="field" style="left:91px;top:980px;width:333px;height:44px">Coupon code</div>
  <div class="btn" style="left:422px;top:980px;width:111px;height:44px;border-radius:0 5px 5px 0">Check !</div>

  <div class="abs" style="left:585px;top:684px;width:2px;height:138px;background:var(--orange)"></div>

  <h3 class="sub-title" style="left:640px;width:468px;top:487px">Delivery address</h3>
  <div class="field" style="left:640px;top:544px;width:468px;height:44px">Street Address</div>
  <div class="field" style="left:640px;top:602px;width:468px;height:44px">City</div>
  <div class="field" style="left:640px;top:660px;width:468px;height:44px">Country</div>
  <div class="field" style="left:640px;top:718px;width:468px;height:44px">Post code</div>
  <h3 class="sub-title" style="left:640px;width:468px;top:800px">Order sumary</h3>
  <div class="sum-row" style="top:866px"><span>Shipping cost:</span><span>Free</span></div>
  <div class="sum-row" style="top:922px"><span>Total:</span><b style="color:var(--ink)">$0.00</b></div>
  <div class="btn" style="left:640px;top:977px;width:468px;height:44px">Order Product</div>
</section>

<section class="features">
  <div class="feature" style="left:201px">
    <svg width="36" height="36" viewBox="0 0 36 36" fill="#fff"><path d="M9 3h18v9a9 9 0 0 1-18 0z"/><path d="M9 6H3c0 6 3 9 7 9M27 6h6c0 6-3 9-7 9" fill="none" stroke="#fff" stroke-width="2.5"/><rect x="16" y="20" width="4" height="8"/><rect x="10" y="28" width="16" height="4"/></svg>
    Quality guaranteed</div>
  <div class="feature" style="left:485px">
    <svg width="40" height="36" viewBox="0 0 40 36" fill="#fff"><rect x="2" y="6" width="24" height="18"/><path d="M27 11h7l5 7v6H27z"/><circle cx="10" cy="27" r="4"/><circle cx="31" cy="27" r="4"/></svg>
    Home delivery</div>
  <div class="feature" style="left:753px">
    <svg width="32" height="36" viewBox="0 0 32 36" fill="#fff"><path d="M9 15V10a7 7 0 0 1 14 0v5" fill="none" stroke="#fff" stroke-width="3.5"/><rect x="4" y="15" width="24" height="19" rx="2"/></svg>
    Secure payment</div>
</section>

<section class="contact">
  <h3 style="left:138px;top:74px">Lantern Yard</h3>
  <div class="info" style="top:126px"><span class="ico"><svg width="14" height="14" viewBox="0 0 14 14"><path d="M1 7 7 1l6 6M3 6v7h8V6" fill="none" stroke="#f7941d" stroke-width="1.6"/></svg></span><span>1.10.32. de Finibus Bonorum<br>et Malorum</span></div>
  <div class="info" style="top:190px;align-items:center"><span class="ico"><svg width="12" height="16" viewBox="0 0 12 16"><rect x="1.5" y="1" width="9" height="14" rx="1.5" fill="none" stroke="#f7941d" stroke-width="1.6"/></svg></span><span>Call Us : (555) 014-2290</span></div>
  <div class="info" style="top:256px;align-items:center"><span class="ico"><svg width="16" height="12" viewBox="0 0 16 12"><rect x="1" y="1" width="14" height="10" fill="none" stroke="#f7941d" stroke-width="1.6"/><path d="M1 1l7 6 7-6" fill="none" stroke="#f7941d" stroke-width="1.6"/></svg></span><span>Mail Us : hello@lanternyard.example</span></div>

  <h3 style="left:593px;top:72px">CONTACT</h3>
  <p class="abs" style="left:593px;top:122px;font-size:14px;color:#666">Do you have some kind of problem with our products?</p>
  <div class="field" style="left:593px;top:174px;width:469px;height:44px">Your Name</div>
  <div class="field" style="left:593px;top:235px;width:469px;height:44px">Your Email</div>
  <div class="field" style="left:593px;top:290px;width:469px;height:99px;align-items:flex-start;padding-top:12px">Message</div>
  <div class="btn" style="left:593px;top:408px;width:469px;height:42px">Send Message</div>
</section>

<footer class="bottom">
  <p>©copyright 2017 Lantern-Yard.All Rights Reserved</p>
  <div class="btn" style="left:963px;top:36px;width:141px;height:39px;font-size:12px;text-transform:none;font-weight:600">Terms &amp; conditions</div>
</footer>

</body>
</html>
```